Brightford Lingua Partners, LLC

We need a business card that includes information about our business and conveys a reliable business that provides document translation services and interpreters for a variety of corporate and individual clients. We want to come across as professional, reliable, yet approachable. It should include the following on one side:

ESL / ENL Language Classes, Private Lessons, and Online Tutors
PALQE Training and Testing
Translating & Interpreting Services
Contact us about Over-the-Phone Interpreting in over 200 languages
24/7/365
www.brightfordlingua.example

The other side should include (555) 481-3062

Marla Quennick, President
412 Garvin Ave., Ste. 209
Indianapolis, IN 46999
Updates

Please add USA as part of the address. Also, please add mrqquennick@brightfordlinguapartners.example as the e-mail address. Thank you.

Target Market(s)

Business professionals, their families, the international community

Industry/Entity Type

Business

Contact Information for Business Card

24/7/365
www.brightfordlingua.example

(555) 481-3062

Marla Quennick, President
412 Garvin Ave., Ste. 209
Indianapolis, IN 46999
USA

Font styles to use
Sans Serif

Colors

Designer to choose colors to be used in the design.

Requirements
Must have
• See project description
• e-mail address and web address
• Phone number
Nice to have
• a globe
• physical address
Should not have
• Should not have the same color scheme as other agencies in our market in Indiana unless it is blue and black. No purple or yellow.

```html
<!DOCTYPE html>
<html lang="en">
<head>
<meta charset="utf-8">
<title>Brightford Lingua Partners – Business Card</title>
<link href="https://fonts.googleapis.com/css2?family=Work+Sans:wght@400;500;600&display=swap" rel="stylesheet">
<style>
  :root {
    --bg: #3a3a3c;
    --brand-blue: #2392d3;
    --ink: #111111;
    --paper: #ffffff;
    --muted: #555555;
  }
  * { box-sizing: border-box; margin: 0; padding: 0; }
  html, body { width: 1200px; height: 900px; overflow: hidden; }
  body {
    background: var(--bg);
    font-family: "Work Sans", Arial, sans-serif;
    display: flex;
    flex-direction: column;
    align-items: center;
    justify-content: center;
    gap: 18px;
  }
  .card {
    position: relative;
    width: 740px;
    height: 423px;
    border-radius: 26px;
    overflow: hidden;
  }

  /* Back side */
  .card--back {
    background: var(--brand-blue);
    color: var(--paper);
    text-align: center;
  }
  .brand {
    display: flex;
    align-items: center;
    gap: 14px;
  }
  .brand__mark {
    width: 112px;
    height: 112px;
    border-radius: 50%;
    flex: none;
  }
  .brand__name {
    font-weight: 500;
    font-size: 34px;
    line-height: 1.02;
    text-align: left;
  }
  .brand__name small { font-size: 15px; }
  .card--back .brand {
    position: absolute;
    top: 46px;
    left: 210px;
  }
  .card--back .brand__mark { background: var(--paper); border: 4px solid var(--paper); box-shadow: inset 0 0 0 6px var(--brand-blue), inset 0 0 0 10px var(--paper); }
  .services {
    position: absolute;
    top: 196px;
    left: 0;
    width: 100%;
    font-size: 15.5px;
    font-weight: 500;
    line-height: 1.4;
  }
  .services__rule {
    width: 490px;
    height: 1px;
    background: var(--paper);
    margin: 10px auto 8px;
  }

  /* Front side */
  .card--front {
    background: var(--paper);
    color: var(--ink);
  }
  .card--front .brand {
    position: absolute;
    top: 36px;
    left: 40px;
  }
  .card--front .brand__mark { width: 100px; height: 100px; background: var(--brand-blue); border: 3px solid var(--paper); box-shadow: 0 0 0 3px var(--brand-blue); }
  .card--front .brand__name { font-size: 30px; color: var(--ink); }
  .front__rule {
    position: absolute;
    top: 178px;
    left: 40px;
    width: 470px;
    height: 2px;
    background: var(--brand-blue);
  }
  .contact {
    position: absolute;
    top: 222px;
    left: 40px;
    list-style: none;
    font-size: 17px;
    line-height: 1.45;
  }
  .contact li { display: flex; align-items: center; gap: 10px; }
  .contact svg { width: 13px; height: 13px; flex: none; }
  .person {
    position: absolute;
    top: 178px;
    right: 86px;
    text-align: right;
  }
  .person__name {
    color: var(--brand-blue);
    font-size: 36px;
    font-weight: 500;
    letter-spacing: 0.5px;
    text-transform: uppercase;
    line-height: 1.1;
  }
  .person__title { font-size: 19px; color: var(--ink); }
  .accent {
    position: absolute;
    top: 182px;
    right: 28px;
    display: flex;
    gap: 6px;
    height: 70px;
  }
  .accent__black { width: 5px; background: var(--ink); }
  .accent__blue { width: 22px; background: var(--brand-blue); }
  .address {
    position: absolute;
    top: 290px;
    right: 86px;
    font-size: 20px;
    line-height: 1.35;
    text-align: left;
    letter-spacing: 0.5px;
  }
</style>
</head>
<body>

  <section class="card card--back" aria-label="Card back">
    <div class="brand">
      <span class="brand__mark"></span>
      <p class="brand__name">Brightford<br>Lingua<br>Partners <small>LLC</small></p>
    </div>
    <div class="services">
      <p>ESL / ENL Language Classes, Private Lessons, and Online Tutors</p>
      <p>PALQE Training and Testing</p>
      <p>Translating &amp; Interpreting Services</p>
      <div class="services__rule"></div>
      <p>Contact us about Over-the-Phone Interpreting in over 200 languages</p>
      <p>24/7/365</p>
    </div>
  </section>

  <section class="card card--front" aria-label="Card front">
    <div class="brand">
      <span class="brand__mark"></span>
      <p class="brand__name">Brightford<br>Lingua<br>Partners <small>LLC</small></p>
    </div>
    <div class="front__rule"></div>

    <ul class="contact">
      <li>
        <svg viewBox="0 0 16 16" aria-hidden="true"><path fill="#2392d3" d="M3.5 1l2.5 3-1.5 2c1 2 3 4 5 5l2-1.5 3 2.5-1.5 2.5C7 15 1 9 1 2.5z"/></svg>
        (555) 481-3062
      </li>
      <li>
        <svg viewBox="0 0 16 16" aria-hidden="true"><rect x="1" y="3" width="14" height="10" fill="none" stroke="#2392d3" stroke-width="1.6"/><path d="M1 3l7 6 7-6" fill="none" stroke="#2392d3" stroke-width="1.6"/></svg>
        info@brightfordlingua.example
      </li>
      <li>
        <svg viewBox="0 0 16 16" aria-hidden="true"><circle cx="8" cy="8" r="6.5" fill="none" stroke="#2392d3" stroke-width="1.4"/><ellipse cx="8" cy="8" rx="3" ry="6.5" fill="none" stroke="#2392d3" stroke-width="1.2"/><path d="M1.5 8h13" stroke="#2392d3" stroke-width="1.2"/></svg>
        www.brightfordlingua.example
      </li>
    </ul>

    <div class="person">
      <p class="person__name">Marla Quennick</p>
      <p class="person__title">President</p>
    </div>
    <div class="accent"><span class="accent__black"></span><span class="accent__blue"></span></div>

    <p class="address">412 Garvin Ave., Ste. 209<br>Indianapolis, IN 46999 USA</p>
  </section>

</body>
</html>
```